Heron Trade finance web design

We are a newly established business which provides invoice finance to Small Businesses in England and Wales.
Our approach is very much a funder where the small business owner can talk to the decision maker. We will guarantee on receipt of information, a decision within 24 hours.
We are not a bank so the look of the website need to be friendly but professional.
Have two types of people we are trying to attract to the website: 1) partners who are small business owners and 2) introducers who is accountants and commercial brokers who introduce us to the small businesses.
Currently no website, although domain has been reserved.
The design should be:
Professional
“Clean” Look
Designed to convey Trust and Authority.
Appeal to the small business owner.
Must incorporate:
Logo (attached)
Front page:Top tabs to other pages 1) About us 2) Services 3) Introducers 4) Contact us
Need picture and logo on page.
1) About us page- Room for talk about the company, the people and our critera.
2) Services page- We need for what invoice finance is, and 5 boxes for different services we will provide. (link on page to contact us)
3) Introducers page- We need a part for why become an introducer? Who we can help? Why we are different? (link on page to contact us)
4) Contact us page- Office address, email, tel and if possible a map and a contact me part which will email direct to us.
Text will be provided for the design, if we can see the setup of the website we will provide a part for each of the pages to support.
Styles we think convey the correct image:
www.brindlecapital.example
www.tollmarkfs.example
www.qelfunding.example
Small business owners
Finance
5+ page

```html
<!DOCTYPE html>
<html lang="en">
<head>
<meta charset="utf-8">
<title>Heron Trade Finance</title>
<link rel="stylesheet" href="https://fonts.googleapis.com/css2?family=Lato:wght@700&family=Open+Sans:wght@400;600;700&family=Raleway:wght@400;500&display=swap">
<style>
:root{
  --red:#e5343a;
  --red-dark:#c9302c;
  --ink:#1c1c1c;
  --text:#4a4a4a;
  --muted:#777;
  --btn:#2f2f2f;
  --white:#fff;
  --footer:#333333;
  --navy:#17202c;
  --line:#dcdcdc;
}
*{box-sizing:border-box;margin:0;padding:0}
html,body{width:1200px;height:2594px;overflow:hidden}
body{position:relative;background:var(--white);font-family:"Open Sans",Arial,sans-serif;color:var(--text)}
.abs{position:absolute}
.top-rule{left:0;top:0;width:1200px;height:5px;background:var(--red)}

/* header */
.site-header{left:0;top:5px;width:1200px;height:125px}
.brand{left:78px;top:40px;font-family:"Open Sans",Arial,sans-serif;font-weight:700;font-size:34px;color:var(--red);letter-spacing:.5px}
.help-line{right:80px;top:14px;display:flex;align-items:center;gap:22px;font-size:19px}
.help-line .help{color:var(--red);font-family:Georgia,serif}
.help-line .phone{display:flex;align-items:center;gap:8px;color:var(--ink);font-size:19px}
.main-nav{right:80px;top:76px;display:flex;gap:61px;font-size:18px;text-transform:uppercase;color:#444}
.main-nav a{color:inherit;text-decoration:none}
.main-nav a.active{color:var(--red)}

/* hero */
.hero{left:0;top:130px;width:1200px;height:468px}
.hero-photo{position:absolute;inset:0;background:linear-gradient(90deg,#f4f5f7 0%,#eef0f3 38%,#d9dde3 55%,#c7ccd4 72%,#e9ebef 100%)}
.hero-title{left:78px;top:105px;font-family:Lato,Arial,sans-serif;font-weight:700;font-size:60px;color:var(--red-dark);letter-spacing:-.5px}
.hero-sub{left:78px;top:178px;width:520px;font-size:26px;line-height:32px;color:#3a3a3a}
.btn{display:inline-flex;align-items:center;justify-content:center;background:var(--btn);color:var(--white);font-size:20px;text-transform:uppercase;border-radius:3px}
.hero .btn{position:absolute;left:76px;top:270px;width:156px;height:45px}

/* lead capture */
.lead-band{left:0;top:598px;width:1200px;height:187px;background:var(--red)}
.lead-title{position:absolute;left:0;top:28px;width:1200px;text-align:center;font-family:Raleway,Arial,sans-serif;font-size:45px;color:var(--white)}
.field{position:absolute;top:100px;height:51px;border:1px solid rgba(255,255,255,.75);color:rgba(255,255,255,.85);font-size:15px;padding:0 14px;display:flex;align-items:center}
.field.email{left:104px;width:396px}
.field.industry{left:524px;width:396px;justify-content:space-between}
.submit{position:absolute;left:940px;top:100px;width:156px;height:51px;background:var(--white);color:var(--red);font-size:21px;display:flex;align-items:center;justify-content:center;border-radius:2px}

/* welcome */
.section-title{position:absolute;left:0;width:1200px;text-align:center;font-family:Raleway,Arial,sans-serif;font-size:36px;color:var(--ink);text-transform:uppercase}
.section-title span{color:var(--red)}
.welcome{left:0;top:785px;width:1200px;height:477px}
.welcome .section-title{top:38px}
.welcome-photo{position:absolute;left:76px;top:111px;width:451px;height:281px;background:linear-gradient(120deg,#5d6875 0%,#c9ced6 40%,#eef0f2 60%,#7d8794 100%)}
.welcome-copy{position:absolute;left:567px;top:103px;width:560px;font-size:15.3px;line-height:22.8px;color:var(--text)}
.welcome-copy p+p{margin-top:22px}
.welcome .btn{position:absolute;left:565px;top:377px;width:156px;height:47px}

/* services */
.services{left:0;top:1262px;width:1200px;height:453px;background:linear-gradient(180deg,#1a2330 0%,#202b39 50%,#141b25 100%)}
.services .section-title{top:45px;color:var(--white)}
.service-card{position:absolute;top:116px;width:235px;text-align:center}
.service-photo{width:235px;height:157px}
.service-name{margin-top:22px;font-family:Raleway,Arial,sans-serif;font-size:22px;color:var(--red)}
.service-text{margin-top:10px;font-size:15px;line-height:25px;color:#d6d9de}
.service-text .more{color:var(--white);font-size:18px;margin-left:6px}
.service-text .more.on{color:var(--red);text-decoration:underline}

/* testimonials */
.testimonials{left:0;top:1715px;width:1200px;height:495px}
.testimonials .section-title{top:40px}
.quote-box{position:absolute;top:130px;width:514px;height:197px;border:1px solid var(--line);box-shadow:0 2px 5px rgba(0,0,0,.12);background:var(--white);padding:50px 44px 0;text-align:center;font-size:15.3px;line-height:22.8px;color:var(--text)}
.quote-mark{position:absolute;top:-18px;left:50%;width:50px;height:36px;margin-left:-25px;background:var(--white);border:1px solid var(--line);border-bottom:none;border-radius:25px 25px 0 0;text-align:center;color:#bbb;font-family:Georgia,serif;font-size:38px;line-height:44px}
.quote-tail{position:absolute;bottom:-14px;width:26px;height:26px;background:var(--white);border-right:1px solid var(--line);border-bottom:1px solid var(--line);transform:rotate(45deg)}
.client{position:absolute;top:360px;display:flex;align-items:center;gap:20px;font-size:16px;color:var(--text);line-height:27px}
.avatar{width:82px;height:82px;border-radius:50%;border:2px solid var(--red);background:linear-gradient(160deg,#cfd3d8,#8a939d)}

/* footer */
.footer-rule{left:0;top:2210px;width:1200px;height:8px;background:var(--red)}
.site-footer{left:0;top:2218px;width:1200px;height:324px;background:var(--footer);color:#eee}
.foot-head{position:absolute;top:40px;font-family:Raleway,Arial,sans-serif;font-size:19px;color:var(--red)}
.foot-links{position:absolute;left:78px;top:86px;list-style:none;font-size:15px;line-height:25px}
.news{position:absolute;left:316px;top:84px;width:270px;font-size:16px;line-height:23px}
.news .date{font-size:14px;color:#999}
.news hr{border:0;border-top:1px solid #666;margin:14px 0 18px}
.news .more{font-size:14px;color:var(--red)}
.contact-list{position:absolute;left:674px;top:86px;font-size:16px;line-height:23px}
.contact-list li{list-style:none;display:flex;gap:12px;margin-bottom:20px}
.foot-brand{position:absolute;left:972px;top:40px;font-weight:700;font-size:28px;color:var(--white)}
.foot-about{position:absolute;left:939px;top:111px;width:200px;font-size:16px;line-height:23px}
.social{position:absolute;top:229px;width:54px;height:54px;border-radius:50%;border:2px solid #eee}
.social.filled{background:var(--white)}
.legal{left:0;top:2542px;width:1200px;height:52px;background:var(--red);color:var(--white);text-align:center;font-size:15px;line-height:52px}
.legal strong{font-weight:700}
</style>
</head>
<body>
<div class="abs top-rule"></div>

<header class="abs site-header">
  <div class="abs brand">Heron Trade Finance</div>
  <div class="abs help-line">
    <span class="help">How Can we Help</span>
    <span class="phone">
      <svg width="18" height="18" viewBox="0 0 24 24"><path fill="#1c1c1c" d="M6.6 10.8a15.2 15.2 0 0 0 6.6 6.6l2.2-2.2c.3-.3.7-.4 1-.2 1.1.4 2.3.6 3.6.6.6 0 1 .4 1 1V20c0 .6-.4 1-1 1A17 17 0 0 1 3 4c0-.6.4-1 1-1h3.5c.6 0 1 .4 1 1 0 1.3.2 2.5.6 3.6.1.3 0 .7-.2 1z"/></svg>
      123 456 7878
    </span>
  </div>
  <nav class="abs main-nav">
    <a class="active" href="#">Home</a><a href="#">About</a><a href="#">Services</a><a href="#">Introducers</a><a href="#">Contact</a>
  </nav>
</header>

<section class="abs hero">
  <div class="hero-photo" role="img" aria-label="Photo of three colleagues working together at a laptop in a bright office"></div>
  <h1 class="abs hero-title">FINANCIAL SERVICES</h1>
  <p class="abs hero-sub">Lorem Ipsum is simply dummy text of the printing and typesetting industry</p>
  <a class="btn">Read More</a>
</section>

<section class="abs lead-band">
  <h2 class="lead-title">Let's deliver the right solution for You...</h2>
  <div class="field email">E mail</div>
  <div class="field industry">Industry
    <svg width="26" height="14" viewBox="0 0 26 14"><path d="M0 0h26L13 14z" fill="rgba(255,255,255,.8)"/></svg>
  </div>
  <div class="submit">SUBMIT</div>
</section>

<section class="abs welcome">
  <h2 class="section-title">Welcome to <span>Heron</span></h2>
  <div class="welcome-photo" role="img" aria-label="Photo of a businesswoman presenting at a flip chart to colleagues"></div>
  <div class="welcome-copy">
    <p>Lorem Ipsum is simply dummy text of the printing and typesetting industry. Lorem Ipsum has been the industry's standard dummy text ever since the 1500s, when an unknown printer took a galley of type and scrambled it to make a type specimen book.It has survived not only five centuries, but also the leap into electronic typesetting, remaining essentially unchanged.</p>
    <p>Lorem Ipsum is simply dummy text of the printing and typesetting industry. Lorem Ipsum has been the industry's standard dummy text ever since the 1500s, when an unknown printer took a galley of type and scrambled it to make a type specimen book.It has survived not only five centuries, but also the leap into electronic typesetting, remaining essentially unchanged.</p>
  </div>
  <a class="btn">Read More</a>
</section>

<section class="abs services">
  <h2 class="section-title">Our <span>Services</span></h2>
  <div class="service-card" style="left:76px">
    <div class="service-photo" role="img" aria-label="Photo of a hand holding a smartphone showing charts" style="background:linear-gradient(135deg,#2c4f7a,#8fb3d6,#dfe8f1)"></div>
    <div class="service-name">Lorem Ipsum is simply</div>
    <div class="service-text">Lorem Ipsum is simply dummy text of the printing and typesetting... <span class="more on">READ MORE</span></div>
  </div>
  <div class="service-card" style="left:347px">
    <div class="service-photo" role="img" aria-label="Illustration of colourful 3D bar and pie charts on a report" style="background:linear-gradient(135deg,#f2f3f6,#c9cde8,#6b74c4)"></div>
    <div class="service-name">Lorem Ipsum is simply</div>
    <div class="service-text">Lorem Ipsum is simply dummy text of the printing and typesetting... <span class="more">READ MORE »</span></div>
  </div>
  <div class="service-card" style="left:618px">
    <div class="service-photo" role="img" aria-label="Photo of a calculator and pen over financial forms" style="background:linear-gradient(135deg,#d8d9dc,#f2f2f2,#9a9ea6)"></div>
    <div class="service-name">Lorem Ipsum is simply</div>
    <div class="service-text">Lorem Ipsum is simply dummy text of the printing and typesetting... <span class="more">READ MORE »</span></div>
  </div>
  <div class="service-card" style="left:889px">
    <div class="service-photo" role="img" aria-label="Photo of a financial statement document with a pen" style="background:linear-gradient(135deg,#c5dcf3,#7fa9d8,#e7eef7)"></div>
    <div class="service-name">Lorem Ipsum is simply</div>
    <div class="service-text">Lorem Ipsum is simply dummy text of the printing and typesetting... <span class="more">READ MORE »</span></div>
  </div>
</section>

<section class="abs testimonials">
  <h2 class="section-title">What People <span>Are Saying</span></h2>
  <div class="quote-box" style="left:76px">
    <div class="quote-mark">&#8221;</div>
    Lorem Ipsum is simply dummy text of the printing and typesetting industry. Lorem Ipsum has been the industry's standard dummy text ever since the 1500s, when an unknown printer took a galley of type and scrambled it to make a type specimen book.
    <div class="quote-tail" style="left:50px"></div>
  </div>
  <div class="client" style="left:86px">
    <div class="avatar" role="img" aria-label="Customer portrait photo"></div>
    <div>Customer Name<br>Client</div>
  </div>
  <div class="quote-box" style="left:610px">
    <div class="quote-mark">&#8221;</div>
    Lorem Ipsum is simply dummy text of the printing and typesetting industry. Lorem Ipsum has been the industry's standard dummy text ever since the 1500s, when an unknown printer took a galley of type and scrambled it to make a type specimen book.
    <div class="quote-tail" style="right:50px"></div>
  </div>
  <div class="client" style="right:86px;text-align:right">
    <div>Customer Name<br>Client</div>
    <div class="avatar" role="img" aria-label="Customer portrait photo"></div>
  </div>
</section>

<div class="abs footer-rule"></div>
<footer class="abs site-footer">
  <div class="foot-head" style="left:78px">Useful Links</div>
  <ul class="foot-links"><li>Home</li><li>About us</li><li>Services</li><li>Introducer</li><li>News</li><li>Contact</li></ul>

  <div class="foot-head" style="left:316px">Latest News</div>
  <div class="news">
    Lorem Ipsum is simply dummy text of the printing and typesetting.<br><span class="date">5th june,2016</span>
    <hr>
    Lorem Ipsum is simply dummy text of the printing and typesetting.<br><span class="date">5th june,2016</span><br><span class="more">Read More »</span>
  </div>

  <div class="foot-head" style="left:674px">Get in touch with us</div>
  <ul class="contact-list">
    <li><svg width="16" height="20" viewBox="0 0 16 20"><path fill="#bbb" d="M8 0a8 8 0 0 0-8 8c0 6 8 12 8 12s8-6 8-12a8 8 0 0 0-8-8zm0 11a3 3 0 1 1 0-6 3 3 0 0 1 0 6z"/></svg><span style="margin-left:12px">123,Lorem Ipsum,<br>Country,Zip Code.</span></li>
    <li><svg width="18" height="18" viewBox="0 0 24 24"><path fill="#bbb" d="M6.6 10.8a15.2 15.2 0 0 0 6.6 6.6l2.2-2.2c.3-.3.7-.4 1-.2 1.1.4 2.3.6 3.6.6.6 0 1 .4 1 1V20c0 .6-.4 1-1 1A17 17 0 0 1 3 4c0-.6.4-1 1-1h3.5c.6 0 1 .4 1 1 0 1.3.2 2.5.6 3.6.1.3 0 .7-.2 1z"/></svg><span style="margin-left:10px">123 456 7878</span></li>
    <li><svg width="20" height="16" viewBox="0 0 20 16"><rect x="1" y="1" width="18" height="14" fill="none" stroke="#bbb" stroke-width="1.6"/><path d="M1 1l9 7 9-7" fill="none" stroke="#bbb" stroke-width="1.6"/></svg><span style="margin-left:8px">hello@herontradefinance.example</span></li>
  </ul>

  <div class="foot-brand">Heron Trade</div>
  <p class="foot-about">Lorem Ipsum is simply dummy text of the printing and typesetting.</p>
  <span class="social filled" style="left:944px" aria-label="Social link"></span>
  <span class="social" style="left:1006px" aria-label="Social link"></span>
  <span class="social" style="left:1068px" aria-label="Social link"></span>
</footer>

<div class="abs legal">© <strong>Heron Trade Finance Limited</strong> - 2016 All Right Reserved</div>
</body>
</html>
```